Velvet Dawn Site Make Over

I would like to get a site makeover for www.velvetdawn.example. The two main pages are the products pages eg: http://www.velvetdawn.example.au/products/miravelle.html

and the home page. Please focus more on the products page as it is 10x more important than the home page.

The width of the pages should be 990px.
Updates

Project Deadline Extended
Reason: Designers require extra time to finish submissions

Target Market(s)

WOmen aged 18-35

Industry/Entity Type

Club

Requirements
Must have
• must be "pretty"

```html
<!DOCTYPE html>
<html lang="en">
<head>
<meta charset="utf-8">
<title>Velvet Dawn — Home</title>
<link rel="stylesheet" href="https://fonts.googleapis.com/css2?family=Merriweather:wght@300;400;700;900&display=swap">
<style>
  :root {
    --pink: #e0137f;
    --bar: #232323;
    --bar-text: #ffffff;
    --backdrop: #e4e0e6;
    --backdrop-deep: #d6d0d9;
    --panel: #ffffff;
  }
  * { margin: 0; padding: 0; box-sizing: border-box; }
  html, body { width: 1200px; height: 962px; overflow: hidden; }
  body {
    position: relative;
    font-family: "Merriweather", Georgia, serif;
    background: var(--panel);
  }
  a { text-decoration: none; color: inherit; }

  .backdrop {
    position: absolute; left: 0; top: 64px; width: 1200px; height: 827px;
    background: radial-gradient(ellipse at 30% 40%, var(--backdrop) 0%, var(--backdrop-deep) 100%);
  }

  .top-bar {
    position: absolute; left: 0; top: 0; width: 1200px; height: 64px;
    background: var(--bar); color: var(--bar-text); font-size: 15px;
  }
  .top-bar a { position: absolute; top: 35px; line-height: 20px; transform: translateY(-50%); white-space: nowrap; }
  .top-bar .current { font-weight: 700; }

  .brand { position: absolute; left: 69px; top: 102px; width: 312px; text-align: center; color: var(--pink); }
  .brand-name { font-size: 35px; font-weight: 300; line-height: 52px; letter-spacing: 1px; }
  .brand-tagline { font-size: 11.5px; margin-top: 6px; }

  .search { position: absolute; left: 846px; top: 80px; display: flex; gap: 9px; }
  .search-field {
    width: 242px; height: 26px; background: #fff;
    font-size: 14px; color: #8a8a8a; padding: 0 6px; line-height: 26px;
  }
  .search-go { width: 28px; height: 26px; background: #fff; display: flex; align-items: center; justify-content: center; }
  .account-links { position: absolute; top: 112px; left: 0; font-size: 12.5px; color: var(--pink); }
  .account-links a { position: absolute; white-space: nowrap; }

  .showcase { position: absolute; left: 69px; top: 202px; width: 1058px; height: 591px; background: var(--panel); overflow: hidden; }
  .showcase-photo {
    position: absolute; right: 0; top: 0; width: 360px; height: 591px;
    background: linear-gradient(90deg, #ffffff 0%, #f2ded2 28%, #e8c4ad 60%, #b08060 85%, #5a3a26 100%);
  }

  .category-nav { position: absolute; left: 44px; top: 54px; }
  .category-nav a {
    display: block; width: 167px; height: 73px; line-height: 70px;
    font-size: 23px; color: var(--pink); letter-spacing: 0.5px;
    border-bottom: 1px solid var(--pink);
  }
  .category-nav a:first-child { height: 71px; }

  .sale-banner {
    position: absolute; left: 399px; top: 161px; width: 255px;
    text-align: center; color: var(--pink); font-size: 40px; line-height: 39px;
    border-bottom: 1px solid var(--pink); padding-bottom: 15px;
  }
  .sale-banner .strong { font-weight: 900; }
  .sale-banner .light { font-weight: 300; }

  .footer {
    position: absolute; left: 2px; top: 891px; width: 1198px; height: 71px;
    background: var(--bar); color: var(--bar-text); font-size: 15px;
  }
  .footer a { position: absolute; top: 34px; transform: translateY(-50%); white-space: nowrap; }
</style>
</head>
<body>
  <div class="backdrop" role="img" aria-label="Soft lilac damask wallpaper pattern"></div>

  <nav class="top-bar">
    <a class="current" href="#" style="left:69px">Home</a>
    <a href="#" style="left:151px">Shop Online</a>
    <a href="#" style="left:278px">Shipping</a>
    <a href="#" style="left:384px">About Us</a>
    <a href="#" style="left:490px">Contact Us</a>
    <a href="#" style="left:821px">My Account</a>
    <a href="#" style="left:945px">My Wishlist</a>
    <a href="#" style="left:1067px">My Cart</a>
  </nav>

  <header class="brand">
    <div class="brand-name">Velvet Dawn</div>
    <div class="brand-tagline">Soft Colour for Every Morning</div>
  </header>

  <form class="search">
    <div class="search-field">Search...</div>
    <div class="search-go">
      <svg width="20" height="16" viewBox="0 0 20 16" aria-hidden="true">
        <path d="M1 1 L19 8 L1 15 L5 8 Z" fill="#e0137f"/>
      </svg>
    </div>
  </form>
  <div class="account-links">
    <a href="#" style="left:853px">REGISTER</a>
    <a href="#" style="left:947px">LOGIN</a>
  </div>

  <main class="showcase">
    <nav class="category-nav">
      <a href="#">HAIR CARE</a>
      <a href="#">SKIN CARE</a>
      <a href="#">FRAGRANCES</a>
      <a href="#">MAKE UP</a>
      <a href="#">BLOG</a>
      <a href="#">FORUM</a>
    </nav>

    <div class="sale-banner">
      <div class="strong">SHOP</div>
      <div class="light">THE ONLINE</div>
      <div class="strong">AUTUMN</div>
      <div class="strong">WINTER</div>
      <div class="light">2010 SALE</div>
    </div>

    <div class="showcase-photo" role="img" aria-label="Portrait photograph of a young woman with fresh natural makeup"></div>
  </main>

  <footer class="footer">
    <a href="#" style="left:343px">Terms and Conditions</a>
    <a href="#" style="left:542px">Sitemap</a>
    <a href="#" style="left:638px">Privacy Policy</a>
    <a href="#" style="left:777px">Contact Us</a>
  </footer>
</body>
</html>
```